PowerPoint design of key models

We recently had a new PPT template created which we are very happy with. Now we want to have some of our key models on various pages in PPT to be reformatted and redesigned to match the other graphics of the new PT template. Can you please redesign the models and graphics so they have the same look and feel as the new template. I have included both files for you to work with. Thank you.

```html
<!DOCTYPE html>
<html lang="en">
<head>
<meta charset="utf-8">
<title>Coaching Models – Slide Set</title>
<link href="https://fonts.googleapis.com/css2?family=Fira+Sans:ital,wght@0,400;0,500;0,600;0,700;1,600;1,700&display=swap" rel="stylesheet">
<style>
  :root{
    --navy:#1e2456;
    --sky:#35b5e8;
    --blue:#1a73c9;
    --lav:#dde2f2;
    --lav2:#eceff8;
    --mid:#8190c2;
    --grey:#d4d4d8;
    --ink:#1b1b1f;
    --white:#ffffff;
  }
  *{box-sizing:border-box;margin:0;padding:0}
  html,body{width:1200px;height:847px;overflow:hidden;background:var(--white)}
  body{position:relative;font-family:"Fira Sans",Arial,sans-serif;color:var(--ink)}
  .slide{position:absolute;width:400px;height:282px;overflow:hidden;background:var(--white)}
  .abs{position:absolute}
  .divider-v{position:absolute;top:0;width:1.5px;height:847px;background:var(--sky)}
  .divider-h{position:absolute;left:0;width:1200px;height:1px;background:var(--sky)}

  .brand{position:absolute;display:flex;align-items:center;gap:2px;font-size:6.5px;font-weight:600;color:var(--navy)}
  .brand .dot{width:8px;height:8px;border-radius:50%;background:var(--blue)}
  .title{position:absolute;font-weight:600;color:var(--navy);white-space:nowrap}
  .title::before{content:"";position:absolute;left:-20px;top:55%;width:17px;height:3px;background:var(--blue)}

  .footer .url{position:absolute;left:14px;top:265px;font-size:4.5px;color:#333}
  .footer .bar{position:absolute;left:68px;top:263px;width:290px;height:10px;background:linear-gradient(90deg,var(--sky),var(--blue));transform:skewX(-20deg);display:flex;align-items:center;justify-content:center}
  .footer .bar span{font-size:3.5px;color:#e8f4ff;transform:skewX(20deg)}
  .footer .num{position:absolute;left:361px;top:263px;width:22px;height:10px;background:var(--navy);transform:skewX(-20deg);color:#fff;font-size:5.5px;font-weight:600;display:flex;align-items:center;justify-content:center}

  /* tables */
  .cell{position:absolute;font-size:4px;padding:1px 2px;line-height:1.2;overflow:hidden}
  .hd{background:var(--navy);color:#fff;font-weight:500}
  .sky{background:var(--sky);color:#fff;font-weight:600}
  .lv{background:var(--lav)}
  .lv2{background:var(--lav2)}
  .md{background:var(--mid);color:#fff}
  .gr{background:var(--grey)}
  .noteBox{position:absolute;border:1px solid var(--sky);border-radius:6px;background:#e2ecf8;font-size:4.6px;padding:4px 6px;line-height:1.9}
  .noteBox .hl{color:var(--sky)}

  /* listening */
  .lvl{position:absolute;left:44px;width:251px;height:26px;border-radius:2px;color:#fff;font-size:10px;display:flex;align-items:center;padding-left:11px}
  .lvl.n{background:var(--navy)} .lvl.s{background:var(--sky)}
  .tag{position:absolute;left:309px;width:66px;height:25px;background:var(--sky);border-radius:2px;color:#fff;font-size:7.5px;text-align:center;line-height:1.25;display:flex;align-items:center;justify-content:center}

  /* active listening */
  .step{position:absolute;left:33px;width:112px;height:26px;color:#fff;font-size:10.5px;font-weight:600;display:flex;align-items:center;justify-content:center}
  .bul{position:absolute;left:175px;font-size:8.6px;line-height:1.35;width:215px}
  .bul::before{content:"";position:absolute;left:-12px;top:4px;width:3px;height:3px;border-radius:50%;background:var(--sky)}

  .ph{position:absolute;border-radius:4px}
  .colhd{position:absolute;font-size:10.5px;font-weight:600;color:var(--sky);text-align:center;width:120px}
  .list{position:absolute;font-size:8.6px;text-align:center;line-height:1.68;width:120px}

  .tick-row{position:absolute;left:24px;width:181px;height:15px;font-size:7.6px;display:flex;align-items:center;padding-left:4px;border-bottom:1px solid #fff}
  .tick-row .tk{position:absolute;right:0;top:0;width:19px;height:14px;display:flex;align-items:center;justify-content:center;color:#d8232a;font-size:7px;border-left:1px solid #fff}

  .navyBox{position:absolute;background:var(--navy);color:#fff;font-weight:600;display:flex;align-items:center;justify-content:center;text-align:center}
  .obj{position:absolute;left:242px;font-size:10.5px;font-weight:600;color:var(--navy)}
</style>
</head>
<body>

<!-- Slide 45: Coaching Action Tool -->
<section class="slide" style="left:0;top:0">
  <div class="brand" style="left:324px;top:18px"><span class="dot"></span>Summit Training</div>
  <h1 class="title" style="left:41px;top:28px;font-size:13.5px">The components of the Coaching Action Tool</h1>
  <div class="abs" style="left:47px;top:44px;font-size:6px;color:var(--sky)">Front – CAT Assessment</div>

  <div class="cell hd" style="left:18px;top:52px;width:123px;height:8px;font-size:3.6px">OBSERVATION</div>
  <div class="cell md" style="left:142px;top:52px;width:113px;height:8px;font-size:3.2px">OFF TRACK</div>
  <div class="cell md" style="left:256px;top:52px;width:122px;height:8px;font-size:3.2px">ON TRACK</div>
  <div class="cell sky" style="left:18px;top:62px;width:360px;height:9px;font-size:5.5px">BEHAVIOURS &amp; CULTURE</div>
  <div class="cell lv2" style="left:18px;top:73px;width:123px;height:13px">1. Lives our value- BE GREAT</div>
  <div class="cell lv2" style="left:142px;top:73px;width:113px;height:13px"></div>
  <div class="cell lv2" style="left:256px;top:73px;width:122px;height:13px"></div>
  <div class="cell lv" style="left:18px;top:87px;width:123px;height:13px">2. Embodies our 7 virtues</div>
  <div class="cell lv" style="left:142px;top:87px;width:113px;height:13px"></div>
  <div class="cell lv" style="left:256px;top:87px;width:122px;height:13px"></div>
  <div class="cell lv2" style="left:18px;top:101px;width:123px;height:12px">3. Practises Safety and inclusion</div>
  <div class="cell lv2" style="left:142px;top:101px;width:113px;height:12px"></div>
  <div class="cell lv2" style="left:256px;top:101px;width:122px;height:12px"></div>
  <div class="cell hd" style="left:18px;top:114px;width:360px;height:11px;font-size:5.8px">COMPETENCY CLUSTERS</div>
  <div class="cell sky" style="left:18px;top:126px;width:123px;height:11px;font-size:5.5px">P- PLANNING</div>
  <div class="cell md" style="left:142px;top:126px;width:71px;height:11px">Growth (Toward the Standard)</div>
  <div class="cell md" style="left:214px;top:126px;width:63px;height:11px">Great (Achieving standard)</div>
  <div class="cell md" style="left:278px;top:126px;width:59px;height:11px">Good (Above Standard)</div>
  <div class="cell md" style="left:338px;top:126px;width:40px;height:11px">Not observed</div>
  <div class="cell lv" style="left:18px;top:138px;width:123px;height:11px">4. Macro</div>
  <div class="cell lv" style="left:142px;top:138px;width:71px;height:11px"></div>
  <div class="cell lv" style="left:214px;top:138px;width:63px;height:11px"></div>
  <div class="cell lv" style="left:278px;top:138px;width:59px;height:11px"></div>
  <div class="cell lv" style="left:338px;top:138px;width:40px;height:11px"></div>
  <div class="cell lv2" style="left:18px;top:150px;width:123px;height:11px">5. Micro</div>
  <div class="cell lv2" style="left:142px;top:150px;width:71px;height:11px"></div>
  <div class="cell lv2" style="left:214px;top:150px;width:63px;height:11px"></div>
  <div class="cell lv2" style="left:278px;top:150px;width:59px;height:11px"></div>
  <div class="cell lv2" style="left:338px;top:150px;width:40px;height:11px"></div>
  <div class="abs lv2" style="left:18px;top:162px;width:360px;height:49px"></div>
  <div class="noteBox" style="left:22px;top:165px;width:352px;height:42px;background:#fff;line-height:1.55;font-size:4.6px;color:var(--navy)">
    <b>User Instructions</b><br>
    ○ Consultant becomes familiar with performance standards<br>
    ○ Consultant completes self-assessment before a coaching session<br>
    ○ Consultant submits self-assessment before the coaching session<br>
    ○ The coach &amp; Coachee confirm assessment together towards the end of the session
  </div>
  <div class="noteBox" style="left:18px;top:216px;width:360px;height:44px;line-height:2">
    Three BD highlights noted from the session <span class="hl">(BD highlights noted from the session)</span><br><b>1.</b><br><b>2.</b><br><b>3.</b>
  </div>
  <div class="footer"><span class="url">www.summittraining.example</span><div class="bar"><span>Copyright @Summit Training 2024</span></div><div class="num">45</div></div>
</section>

<!-- Slide 46: Three-point observation -->
<section class="slide" style="left:400px;top:0">
  <div class="brand" style="left:327px;top:18px"><span class="dot"></span>Summit Training</div>
  <div class="cell hd" style="left:27px;top:44px;width:119px;height:21px;font-size:5.5px">OBSERVATION</div>
  <div class="cell hd" style="left:147px;top:44px;width:241px;height:12px;font-size:6px;text-align:center">Three-point Observation</div>
  <div class="cell hd" style="left:147px;top:57px;width:73px;height:8px;font-size:3.8px">Growth (Toward the Standard)</div>
  <div class="cell hd" style="left:221px;top:57px;width:67px;height:8px;font-size:3.8px">Great (Achieving standard)</div>
  <div class="cell hd" style="left:289px;top:57px;width:60px;height:8px;font-size:3.8px">Good (Above Standard)</div>
  <div class="cell hd" style="left:350px;top:57px;width:38px;height:8px;font-size:3.8px">Not observed</div>
  <svg class="abs" style="left:27px;top:66px" width="361" height="145" viewBox="0 0 361 145">
    <g fill="#dde2f2">
      <rect x="120" y="0" width="73" height="11"/><rect x="194" y="0" width="67" height="11"/><rect x="262" y="0" width="60" height="11"/>
    </g>
  </svg>
  <div class="cell sky" style="left:27px;top:66px;width:119px;height:11px;font-size:5.3px">R- RECRUIT BD Process</div>
  <div class="cell lv" style="left:27px;top:78px;width:119px;height:11px;font-size:5px">6. R Relationship developed</div>
  <div class="cell lv2" style="left:27px;top:90px;width:119px;height:11px;font-size:5px">7. E Explore Needs <span style="color:var(--sky)">(Specific Behaviours)</span></div>
  <div class="cell lv" style="left:27px;top:102px;width:119px;height:11px;font-size:5px">8. C Collaborate or solution</div>
  <div class="cell lv2" style="left:27px;top:114px;width:119px;height:11px;font-size:5px">9. Review Progress</div>
  <div class="cell lv" style="left:27px;top:126px;width:119px;height:11px;font-size:5px">10. U Uncover &amp; overcome objections</div>
  <div class="cell lv2" style="left:27px;top:138px;width:119px;height:11px;font-size:5px">11. Initiate Commitment</div>
  <div class="cell lv" style="left:27px;top:150px;width:119px;height:11px;font-size:5px">12. T Take action to Execute</div>
  <div class="cell sky" style="left:27px;top:162px;width:119px;height:11px;font-size:5.3px">E- EXECUTE OUTCOMES</div>
  <div class="cell lv2" style="left:27px;top:174px;width:119px;height:11px;font-size:5px">13. Order processing &amp; administration</div>
  <div class="cell sky" style="left:27px;top:186px;width:119px;height:11px;font-size:5.3px">S- SUSTAIN</div>
  <div class="cell lv" style="left:27px;top:198px;width:119px;height:12px;font-size:5px">14. Service excellence follow up</div>
  <svg class="abs" style="left:147px;top:66px" width="241" height="145" viewBox="0 0 241 145">
    <g>
      <rect x="0" y="0" width="241" height="11" fill="#dde2f2"/>
      <rect x="0" y="12" width="241" height="11" fill="#dde2f2"/><rect x="0" y="24" width="241" height="11" fill="#eceff8"/>
      <rect x="0" y="36" width="241" height="11" fill="#dde2f2"/><rect x="0" y="48" width="241" height="11" fill="#eceff8"/>
      <rect x="0" y="60" width="241" height="11" fill="#dde2f2"/><rect x="0" y="72" width="241" height="11" fill="#eceff8"/>
      <rect x="0" y="84" width="241" height="11" fill="#dde2f2"/><rect x="0" y="96" width="241" height="11" fill="#dde2f2"/>
      <rect x="0" y="108" width="241" height="11" fill="#eceff8"/><rect x="0" y="120" width="241" height="11" fill="#dde2f2"/>
      <rect x="0" y="132" width="241" height="12" fill="#dde2f2"/>
      <rect x="203" y="0" width="38" height="144" fill="#d4d4d8"/>
      <g stroke="#fff" stroke-width="1"><line x1="73.5" y1="0" x2="73.5" y2="144"/><line x1="141.5" y1="0" x2="141.5" y2="144"/><line x1="202.5" y1="0" x2="202.5" y2="144"/></g>
    </g>
  </svg>
  <div class="noteBox" style="left:27px;top:213px;width:361px;height:41px;line-height:2.05">
    Key Coaching Conversation/Direction from the session <span class="hl">(Coaching highlights noted from the session)</span><br><b>1.</b><br><b>2.</b><br><b>3.</b>
  </div>
  <div class="footer"><span class="url">www.summittraining.example</span><div class="bar"><span>Copyright @Summit Training 2024</span></div><div class="num">46</div></div>
</section>

<!-- Slide 47: 5 levels of listening -->
<section class="slide" style="left:800px;top:0">
  <div class="brand" style="left:330px;top:18px"><span class="dot"></span>Summit Training</div>
  <h1 class="title" style="left:65px;top:26px;font-size:15px">5 levels of listening</h1>
  <div class="lvl n" style="top:70px">1. Disconnected listening</div>
  <div class="lvl s" style="top:104px">2. Insincere listening</div>
  <div class="lvl n" style="top:137px">3. Selective listening</div>
  <div class="lvl s" style="top:171px">4. Attentive listening</div>
  <div class="lvl n" style="top:205px">5. Empathic listening</div>
  <div class="tag" style="top:69px">It’s all about<br>ME</div>
  <svg class="abs" style="left:333px;top:104px" width="18" height="94" viewBox="0 0 18 94"><rect x="6" y="0" width="6" height="84" fill="#35b5e8"/><polygon points="0,82 18,82 9,94" fill="#35b5e8"/></svg>
  <div class="tag" style="top:205px;left:310px">Now it’s about<br>THEM</div>
  <div class="footer"><span class="url">www.summittraining.example</span><div class="bar"><span>Copyright @Summit Training 2024</span></div><div class="num">47</div></div>
</section>

<!-- Slide 48: Active listening -->
<section class="slide" style="left:0;top:282px">
  <div class="brand" style="left:324px;top:15px"><span class="dot"></span>Summit Training</div>
  <h1 class="title" style="left:49px;top:23px;font-size:15px">Active Listening Skills</h1>
  <div class="step" style="top:57px;background:var(--navy)">Attending</div>
  <svg class="abs" style="left:79px;top:83px" width="20" height="12" viewBox="0 0 20 12"><rect x="6" y="0" width="8" height="5" fill="#1e2456"/><polygon points="0,4 20,4 10,12" fill="#1e2456"/></svg>
  <div class="step" style="top:97px;background:var(--sky)">Following</div>
  <svg class="abs" style="left:79px;top:123px" width="20" height="12" viewBox="0 0 20 12"><rect x="6" y="0" width="8" height="5" fill="#35b5e8"/><polygon points="0,4 20,4 10,12" fill="#35b5e8"/></svg>
  <div class="step" style="top:137px;background:var(--navy)">Reflecting</div>
  <div class="bul" style="top:59px">Log on with your genuine focus, gestures and body language</div>
  <div class="bul" style="top:99px">Question, prompt and probe</div>
  <div class="bul" style="top:138px">Summarise back &amp; check understanding</div>
  <div class="ph" role="img" aria-label="Photo of two colleagues in a coaching conversation" style="left:33px;top:174px;width:109px;height:73px;background:linear-gradient(135deg,#b9a58f,#e4dcd2 55%,#c9ccd3)"></div>
  <div class="abs" style="left:200px;top:196px;font-size:11px;font-weight:600;color:var(--sky)">Let’s practise this skill!</div>
  <div class="footer"><span class="url">www.summittraining.example</span><div class="bar"><span>Copyright @Summit Training 2024</span></div><div class="num">48</div></div>
</section>

<!-- Slide 49: Questioning techniques -->
<section class="slide" style="left:400px;top:282px">
  <div class="brand" style="left:322px;top:17px"><span class="dot"></span>Summit Training</div>
  <h1 class="title" style="left:57px;top:24px;font-size:15px">Questioning Techniques Summary</h1>
  <div class="colhd" style="left:25px;top:45px">Core Questions</div>
  <div class="colhd" style="left:147px;top:45px">Leading Questions</div>
  <div class="colhd" style="left:260px;top:45px;width:132px">Conditional Questions</div>
  <div class="abs" style="left:149px;top:46px;width:1px;height:200px;background:#e2b070"></div>
  <div class="abs" style="left:265px;top:46px;width:1px;height:200px;background:#e2b070"></div>
  <svg class="abs" style="left:26px;top:66px" width="117" height="106" viewBox="0 0 117 106">
    <path d="M0,6 L117,6 L68,70 L68,104 L47,104 L47,70 Z" fill="#1e2456"/>
    <path d="M47,100 Q57,107 68,100 L68,104 L47,104 Z" fill="#1e2456"/>
    <ellipse cx="58.5" cy="6" rx="58.5" ry="6" fill="#35b5e8"/>
    <g stroke="#8a93bd" stroke-width="0.6"><line x1="18" y1="35" x2="98" y2="35"/><line x1="33" y1="55" x2="83" y2="55"/></g>
  </svg>
  <div class="abs" style="left:26px;top:68px;width:117px;text-align:center;font-size:6.2px;font-weight:600;color:#fff">Must be in rapport!</div>
  <div class="abs" style="left:26px;top:90px;width:117px;text-align:center;font-size:6px;color:#fff">Open Questions</div>
  <div class="abs" style="left:26px;top:111px;width:117px;text-align:center;font-size:6px;color:#fff">Closed Questions</div>
  <div class="abs" style="left:26px;top:129px;width:117px;text-align:center;font-size:6px;color:#fff;line-height:1.3">Summary<br>Q’s</div>
  <div class="abs" style="left:25px;top:176px;width:120px;text-align:center;font-size:8.6px;font-weight:600">Qualified Needs</div>
  <div class="list" style="left:25px;top:189px">Open<br>Closed<br>Summary</div>
  <div class="ph" role="img" aria-label="Photo of a consultant presenting ideas on a glass board" style="left:172px;top:64px;width:80px;height:101px;border-radius:0;border:1px solid #8aa;background:linear-gradient(160deg,#dfe7ee,#9b8e80 55%,#6d6a62)"></div>
  <div class="list" style="left:147px;top:189px">Discovery Shortcut<br>Menu Questions<br>Tie Downs</div>
  <div class="abs" style="left:262px;top:84px;width:132px;text-align:center;font-size:17px;font-weight:700;font-style:italic;color:var(--sky);line-height:1.55">“If I…<br>would you… ”</div>
  <div class="list" style="left:266px;top:187px;line-height:1.7">On a Stated Need<br>On a Question<br>On an Objection<br>On a Demand</div>
  <div class="footer"><span class="url">www.summittraining.example</span><div class="bar"><span>Copyright @Summit Training 2024</span></div><div class="num">49</div></div>
</section>

<!-- Slide 50: So what test -->
<section class="slide" style="left:800px;top:282px">
  <div class="brand" style="left:328px;top:17px"><span class="dot"></span>Summit Training</div>
  <h1 class="title" style="left:55px;top:28px;font-size:15px">Passing the “So What?” test</h1>
  <div class="abs" style="left:33px;top:57px;font-size:10.5px;line-height:1.4">Customers buy <span style="color:var(--sky);font-weight:500">Benefits</span><br>not <span style="color:var(--sky);font-weight:500">Features</span>!</div>
  <div class="abs" style="left:290px;top:68px;width:85px;text-align:right;font-size:9px;line-height:1.35">…you need to talk in THEIR language!</div>
  <svg class="abs" style="left:0;top:0" width="400" height="282" viewBox="0 0 400 282">
    <path d="M44,214 C80,150 150,105 260,90 L255,60 L296,89 L264,128 L262,104 C160,112 95,150 44,214 Z" fill="#1e2456"/>
    <circle cx="79" cy="173" r="3.5" fill="#35b5e8" stroke="#fff" stroke-width="1"/>
    <circle cx="147" cy="128" r="6" fill="#35b5e8" stroke="#fff" stroke-width="1"/>
    <circle cx="225" cy="105" r="8.5" fill="#35b5e8" stroke="#fff" stroke-width="1"/>
  </svg>
  <div class="abs" style="left:73px;top:196px;width:60px;font-size:5px;line-height:1.3">“We offer our educators a range of events, training, info sessions, and even social gatherings.”<br><i style="color:var(--sky);font-weight:600">“Well, so what?”</i></div>
  <div class="abs" style="left:132px;top:150px;width:48px;font-size:5px;line-height:1.3">“These are all tailored to your personal goals.”<br><i style="color:#888">“Yeah better ..but …”</i></div>
  <div class="abs" style="left:200px;top:127px;width:62px;font-size:5px;line-height:1.3">“To help you to grow, to find your ideal role more quickly and open up your options to working across Australia or even overseas.”<br><i style="color:var(--sky);font-weight:600">“Yes, that’s what I really need!”</i></div>
  <div class="footer"><span class="url">www.summittraining.example</span><div class="bar"><span>Copyright @Summit Training 2024</span></div><div class="num">50</div></div>
</section>

<!-- Slide 51: Ten step coaching -->
<section class="slide" style="left:0;top:564px">
  <div class="brand" style="left:317px;top:18px"><span class="dot"></span>Summit Training</div>
  <h1 class="title" style="left:44px;top:25px;font-size:15px">Ten Step Coaching Process</h1>
  <div class="abs" style="left:24px;top:68px;width:181px;height:20px;background:var(--navy);color:#fff;font-size:8px;font-weight:500;display:flex;align-items:center;padding-left:4px">For each call……</div>
  <div class="tick-row lv2" style="top:89px">1. Review the situation<span class="tk">✓</span></div>
  <div class="tick-row lv2" style="top:104px">2. Review call objectives – the WHAT<span class="tk">✓</span></div>
  <div class="tick-row lv2" style="top:119px">3. Review the call plan – the HOW<span class="tk">✓</span></div>
  <div class="tick-row lv2" style="top:134px">4. Final pre-sale check, confirm roles<span class="tk">✓</span></div>
  <div class="tick-row" style="top:149px;background:#4da8e0;color:#fff;font-weight:600">5. In the call; listen and observe<span class="tk" style="color:#fff">✓</span></div>
  <div class="tick-row lv2" style="top:164px">6. Congratulate, briefly<span class="tk">✓</span></div>
  <div class="tick-row lv2" style="top:179px">7. Review versus objectives<span class="tk">✓</span></div>
  <div class="tick-row lv2" style="top:194px">8. Reinforce the positives<span class="tk">✓</span></div>
  <div class="tick-row lv2" style="top:209px">9. Agree improvements<span class="tk">✓</span></div>
  <div class="tick-row lv2" style="top:224px">10. Objectives for the next call recorded<span class="tk">✓</span></div>
  <div class="bul" style="left:235px;top:70px;width:145px;font-size:7.4px">Your Team Leader has been trained to <b>ask questions and not tell</b></div>
  <div class="bul" style="left:235px;top:99px;width:145px;font-size:7.4px">We want you to think this way for all calls, not just on coaching days</div>
  <div class="bul" style="left:235px;top:127px;width:145px;font-size:7.4px"><b>No intervention</b> in the call by the Team Leader – it’s your customer/client, your territory, your development</div>
  <div class="abs" style="left:235px;top:179px;width:127px;height:48px;border:1px solid var(--sky);border-radius:7px;display:flex;align-items:center;justify-content:center;text-align:center;font-size:7.6px;font-weight:600;font-style:italic;color:var(--blue);line-height:1.4">“We want to teach you how to fish …<br>not to feed you for a day!”</div>
  <div class="footer"><span class="url">www.summittraining.example</span><div class="bar"><span>Copyright @Summit Training 2024</span></div><div class="num">51</div></div>
</section>

<!-- Slide 53: Features vs Benefits -->
<section class="slide" style="left:400px;top:564px">
  <div class="brand" style="left:330px;top:16px"><span class="dot"></span>Summit Training</div>
  <h1 class="title" style="left:50px;top:22px;font-size:15px">Distinguishing Features from Benefits</h1>
  <div class="navyBox" style="left:28px;top:70px;width:103px;height:37px;background:var(--sky);border-radius:3px;font-size:10.5px;line-height:1.35">Features &amp;<br>Advantages</div>
  <div class="abs" style="left:146px;top:77px;font-size:17px;color:var(--navy)">VS</div>
  <div class="navyBox" style="left:242px;top:72px;width:61px;height:36px;font-size:10.5px">Benefits</div>
  <svg class="abs" style="left:0;top:0" width="400" height="282" viewBox="0 0 400 282">
    <g stroke="#1a73c9" stroke-width="0.8" fill="none"><path d="M272,108 V116 M196,121 V116 H339 V121 M272,116 V121"/></g>
    <rect x="77" y="113" width="6" height="50" fill="#35b5e8"/><polygon points="70,160 90,160 80,172" fill="#35b5e8"/>
  </svg>
  <div class="navyBox" style="left:171px;top:121px;width:51px;height:40px;font-size:6px;line-height:1.3">For clients &amp; their organisation</div>
  <div class="navyBox" style="left:233px;top:121px;width:61px;height:43px;font-size:6px;line-height:1.3">For Educators &amp; their careers</div>
  <div class="navyBox" style="left:305px;top:121px;width:66px;height:40px;font-size:6px;line-height:1.3">For Learner &amp; their development</div>
  <div class="abs" style="left:30px;top:176px;width:100px;text-align:center;font-size:9px;line-height:1.35">Product/Service<br>Focused</div>
  <div class="abs" style="left:21px;top:203px;width:360px;height:43px;background:var(--sky);border-radius:6px;color:#fff;font-size:12px;display:flex;align-items:center;justify-content:space-between;padding:0 36px 0 32px"><span>Attributes</span><span>Outcomes</span></div>
  <div class="footer"><span class="url" style="top:268px">www.summittraining.example</span><div class="bar" style="top:266px"><span>Copyright @Summit Training 2024</span></div><div class="num" style="top:266px">53</div></div>
</section>

<!-- Slide 55: Handling objections -->
<section class="slide" style="left:800px;top:564px">
  <div class="brand" style="left:327px;top:17px"><span class="dot"></span>Summit Training</div>
  <h1 class="title" style="left:54px;top:22px;font-size:15px">Handling Objections: ABC</h1>
  <svg class="abs" style="left:0;top:0" width="400" height="282" viewBox="0 0 400 282">
    <g stroke="#c8ccd6" stroke-width="0.8" fill="none">
      <path d="M133,110 L150,85 H195"/><path d="M137,140 H195"/><path d="M133,171 L150,194 H195"/>
    </g>
    <circle cx="79" cy="140" r="53" fill="#1e2456"/>
    <g>
      <circle cx="213" cy="85" r="17" fill="#1a73c9"/><circle cx="213" cy="139" r="17" fill="#1a73c9"/><circle cx="213" cy="193" r="17" fill="#1a73c9"/>
    </g>
    <g fill="none" stroke="#fff" stroke-width="1">
      <circle cx="213" cy="85" r="7"/><circle cx="213" cy="85" r="4"/><circle cx="213" cy="85" r="1.3" fill="#fff"/>
      <circle cx="213" cy="139" r="7"/><circle cx="213" cy="139" r="4"/><circle cx="213" cy="139" r="1.3" fill="#fff"/>
      <circle cx="213" cy="193" r="7"/><circle cx="213" cy="193" r="4"/><circle cx="213" cy="193" r="1.3" fill="#fff"/>
      <path d="M213,85 L223,78 M213,139 L223,132 M213,193 L223,186"/>
    </g>
  </svg>
  <div class="abs" style="left:26px;top:121px;width:106px;text-align:center;font-size:9.5px;font-weight:600;color:#fff">Summit Training</div>
  <div class="abs" style="left:26px;top:141px;width:106px;text-align:center;font-size:9px;color:#fff">AS SIMPLE AS:</div>
  <div class="obj" style="top:78px">Acknowledge &amp; Ask</div>
  <div class="obj" style="top:132px">Bundle</div>
  <div class="obj" style="top:186px">Counter &amp; Close</div>
  <div class="footer"><span class="url">www.summittraining.example</span><div class="bar"><span>Copyright @Summit Training 2024</span></div><div class="num">55</div></div>
</section>

<div class="divider-v" style="left:391px"></div>
<div class="divider-v" style="left:798px"></div>
<div class="divider-h" style="top:287px"></div>
<div class="divider-h" style="top:569px"></div>

</body>
</html>
```